The Brackenfell Raffle Competition - Coming Soon Poster

Our company is about to start operating a monthly prize competition, where entrants buy a ticket, answer the question and if they get it correct, have a chance of winning £10,000. Tickets will be mainly sold in pubs and restaurants.

This A3-sized poster will be one of the first ways people hear about The Brackenfell Raffle. Ideally it will be eye-catching, exciting and stylish. It could feature images of money, or things you can do with significant amounts of money.

Whichever design I choose, I hope to create a range of posters and flyers based on the same fundamental themes - so this design is actually the start of the brand image also, and that means more work for the same designer!

I would like the poster to feature some kind of catchy tag-line, like "Get ready to play..." / "Coming Soon..." / "Prepare yourself for...etc.,

- and also instruction on how they will play - for example - 1)Get a ticket 2)Answer the question 3)Cross fingers, or
1)Get a ticket 2)Fill it in 3)Imagine £10,000. Hold that thought.
or
Get a Ticket - Complete the Question - Good luck!

Also, possibly include this:
"Your'e much, much more likely to win £10,000 with The Brackenfell Raffle than a six-number lottery. Why? Because we don't give ridiculously huge prizes that virtually no-one wins, and we'd rather give you more than the price of a round at your local. So we settled with a nice compromise - Ten Grand."

- but overall, its up to you with the design and the wording! If you can think of different wording, give it a go!!

MUST INCLUDE
"We will give 2% of all ticket sales to charities each month."

The cost of entry is £3, the prize(s) are £10,000. The competition will operate monthly, and the first month's competition will start on 1 July 2011. We already have a logo, in lots of different file formats, see attached zip file.

Thank you

Martin

Just an update:

Just a point to note - for some reason the image files such as TIF or PNG that I sent to you have messed up colours. The colours should look like they do in the BMP and JPG files :) the colour codes (RBG) are also in a text file in the zip folder if you need them

Thank you!

Target Market(s)

Adults, in the UK, both male and female. Usually, the target market will be in a pub, bar or restaurant.

Industry/Entity Type

It Company

Requirements
Must have
• A nice sort of 'photoshop feel' - basically something that looks really artistic. Lots of posters can look cheesy or overcrowded.
Nice to have
• Something that can be used again and again in different forms to create brand identity.

Possibly include photos of english money, £20 notes for example.
Should not have
• Should not look cheesy or cheap =]

```html
<!DOCTYPE html>
<html lang="en">
<head>
<meta charset="utf-8">
<title>The Brackenfell Raffle – Coming Soon</title>
<link rel="stylesheet" href="https://fonts.googleapis.com/css2?family=Archivo+Black&family=Arimo:wght@400;700&display=swap">
<style>
  :root {
    --page: #ffffff;
    --glow: #fff700;
    --amber: #f0b418;
    --orange: #e27a22;
    --ember: #d2452c;
    --ink: #000000;
    --light: #ffffff;
    --brand: #c4262e;
    --mark: #e8782a;
    --gold-hi: #ffff4a;
    --gold-mid: #e8e020;
    --gold-lo: #8a7a08;
    --steel-hi: #b0b0b0;
    --steel-lo: #1a1a1a;
  }
  * { margin: 0; padding: 0; box-sizing: border-box; }
  html, body {
    width: 1200px; height: 900px; overflow: hidden;
    background: var(--page);
    font-family: "Arimo", Arial, sans-serif;
  }
  .poster {
    position: absolute; left: 238px; top: 0;
    width: 730px; height: 900px;
    background: radial-gradient(ellipse 75% 70% at 50% 50%, var(--glow) 0%, var(--amber) 45%, var(--orange) 80%, var(--ember) 110%);
    overflow: hidden;
  }
  .poster > * { position: absolute; }
  .brand-mark {
    left: 12px; top: 22px; width: 140px; height: 140px;
    border-radius: 50%; background: var(--mark);
  }
  .brand-name {
    left: 195px; top: 62px;
    font-size: 42px; font-weight: 400; color: var(--brand);
    white-space: nowrap; letter-spacing: 0.5px;
  }
  .tagline {
    left: 0; width: 100%; top: 168px; text-align: center;
    font-size: 62px; font-weight: 700; color: var(--ink);
  }
  .word { color: var(--light); font-weight: 700; white-space: nowrap; line-height: 1; }
  .w-enter { left: 20px; top: 260px; font-size: 50px; }
  .w-for { left: 189px; top: 322px; font-size: 22px; }
  .w-your { left: 232px; top: 294px; font-size: 60px; }
  .w-chance { left: 425px; top: 368px; font-size: 39px; }
  .w-to { left: 55px; top: 432px; font-size: 46px; }
  .w-win { left: 120px; top: 412px; font-size: 70px; }
  .prize {
    left: 14px; top: 486px; white-space: nowrap;
    font-family: "Archivo Black", "Arial Black", sans-serif;
    font-size: 160px; line-height: 1;
    -webkit-text-stroke: 1.5px var(--ink);
  }
  .prize-currency {
    background: linear-gradient(160deg, var(--steel-hi), var(--steel-lo) 55%, #555);
    -webkit-background-clip: text; background-clip: text; color: transparent;
    margin-right: 34px;
  }
  .prize-amount {
    background: linear-gradient(170deg, var(--gold-hi) 20%, var(--gold-mid) 55%, var(--gold-lo) 90%);
    -webkit-background-clip: text; background-clip: text; color: transparent;
    letter-spacing: -6px;
  }
  .how {
    left: 0; width: 100%; top: 703px; text-align: center;
  }
  .how-title { font-size: 20px; font-weight: 700; color: var(--ink); margin-bottom: 12px; }
  .how-steps { list-style: none; }
  .how-steps li {
    font-size: 26px; font-weight: 700; color: var(--light);
    line-height: 40px;
  }
  .charity {
    left: 0; width: 100%; top: 868px; text-align: center;
    font-size: 15px; font-weight: 700; color: var(--ink);
  }
</style>
</head>
<body>
  <main class="poster">
    <div class="brand-mark" aria-hidden="true"></div>
    <div class="brand-name">The Brackenfell Raffle</div>

    <h1 class="tagline">Get Ready...</h1>

    <span class="word w-enter">Enter</span>
    <span class="word w-for">for</span>
    <span class="word w-your">your</span>
    <span class="word w-chance">chance</span>
    <span class="word w-to">to</span>
    <span class="word w-win">win...</span>

    <div class="prize"><span class="prize-currency">£</span><span class="prize-amount">10,000</span></div>

    <section class="how">
      <h2 class="how-title">How it Works</h2>
      <ol class="how-steps">
        <li>1) Get a ticket for just £3</li>
        <li>2) Answer the question on the ticket</li>
        <li>3) Imagine an extra £10,000 in your pocket!</li>
      </ol>
    </section>

    <p class="charity">We will give 2% of all ticket sales to charities each month.</p>
  </main>
</body>
</html>
```